New Brazilian Craft Brewery Needs a Logo and Label Design.

We need a beer logo and label design for our new brazilian brewery. The brewery name is "VELUMAR" (that means holy in portuguese). The logo should have the words "VELUMAR" and "CERVEJAS ARTESANAIS" (craft beer). We would like a logo and label desings with something about holy theme like an angel drinking beer, a glass with wings, or anything else we are open to any new sugestion. We would like to see projects that are not the same tipical and classic beer desing. We like different, inovating, colorfull desings. Attached the are some old desings just for reference as we want something different.
Target Market(s)
Craft beer drinkers.
Industry/Entity Type
Brewery

```html
<!DOCTYPE html>
<html lang="pt-BR">
<head>
<meta charset="utf-8">
<title>Velumar – India Pale Ale label</title>
<link rel="stylesheet" href="https://fonts.googleapis.com/css2?family=Arvo:wght@700&family=Bree+Serif&family=Josefin+Slab:wght@300&display=swap">
<style>
  :root{
    --paper:#ffffff;
    --gold-light:#d8bb4c;
    --gold-dark:#b48d1e;
    --ink-green:#17452a;
    --ribbon:#145759;
    --ribbon-dark:#0c3837;
    --badge:#f2f2ee;
    --white:#f7f6f1;
  }
  *{box-sizing:border-box;margin:0;padding:0}
  html,body{width:1200px;height:1000px;overflow:hidden;background:var(--paper)}
  .canvas{position:relative;width:1200px;height:1000px}
  .label{position:absolute;background:linear-gradient(120deg,var(--gold-light),var(--gold-dark));font-family:"Bree Serif",Georgia,serif;color:var(--ink-green)}
  .label--front{left:152px;top:280px;width:371px;height:692px;border-radius:0 0 16px 16px}
  .label--back{left:675px;top:322px;width:370px;height:650px;border-radius:28px}
  .abs{position:absolute}
  .brand-badge{position:absolute;left:152px;top:14px;width:370px;height:370px;border-radius:50%;background:var(--badge);display:flex;align-items:center;justify-content:center}
  .brand-name{font-family:"Bree Serif",Georgia,serif;font-size:72px;color:var(--ink-green);letter-spacing:2px;margin-top:40px}
  .ribbon{position:absolute}
  .ribbon-text{position:absolute;color:var(--white);text-align:center;font-family:"Bree Serif",Georgia,serif}
  .front-ribbon-text{left:110px;top:330px;width:455px;font-size:30px;letter-spacing:2px}
  .style-name{position:absolute;left:0;width:100%;text-align:center;color:var(--white)}
  .style-india{top:155px;font-family:"Arvo",Georgia,serif;font-weight:700;font-size:92px;letter-spacing:4px}
  .style-pale{top:245px;font-family:"Josefin Slab",Georgia,serif;font-weight:300;font-size:58px;letter-spacing:3px}
  .divider{position:absolute;border-top:2px dashed var(--ink-green);height:0}
  .heading{font-size:25px}
  .small{font-size:14px;line-height:20px}
  .white{color:var(--white)}
  .body-white{font-size:18px;line-height:25px}
  .quote-text{left:660px;top:765px;width:400px;font-size:11.5px;line-height:17px;letter-spacing:0.8px}
  .sticker{position:absolute;left:131px;top:541px;width:207px;height:65px;background:var(--badge)}
</style>
</head>
<body>
<div class="canvas">
  <!-- front label -->
  <div class="label label--front">
    <div class="style-name style-india">INDIA</div>
    <div class="style-name style-pale">PALE ALE</div>
    <div class="abs heading" style="left:31px;top:340px">CERVECA CLARA FORTE</div>
    <div class="abs small" style="left:31px;top:372px">puro malto com ingredientes selecionados</div>
    <div class="divider" style="left:31px;top:412px;width:308px"></div>
    <div class="abs white" style="left:31px;top:440px;font-size:21px">Fome?</div>
    <div class="abs white body-white" style="left:31px;top:470px">combina bem com:<br>carnes vermelhas, queijos fortes<br>e pratos com sabores intensos.</div>
    <div class="divider" style="left:31px;top:577px;width:308px"></div>
    <div class="abs" style="left:31px;top:658px;font-size:16px">600 ml</div>
    <div class="abs" style="right:31px;top:658px;font-size:16px">6,9% vol. alc.</div>
  </div>

  <div class="brand-badge"><span class="brand-name">VELUMAR</span></div>

  <svg class="ribbon" style="left:0;top:0" width="680" height="400" aria-hidden="true">
    <polygon points="45,330 150,330 150,390 45,390 80,360" fill="var(--ribbon-dark)"/>
    <polygon points="628,330 525,330 525,390 628,390 593,360" fill="var(--ribbon-dark)"/>
    <rect x="110" y="320" width="455" height="60" fill="var(--ribbon)"/>
  </svg>
  <div class="ribbon-text front-ribbon-text">CERVEJAS ARTESANAIS</div>

  <!-- back label -->
  <div class="label label--back">
    <div class="abs heading" style="left:30px;top:42px;font-size:27px">CERVECA ARTISANAL</div>
    <div class="abs heading" style="left:30px;top:74px;font-size:24px">Vale Dourado -RS- Brasil</div>
    <div class="divider" style="left:30px;top:119px;width:308px"></div>
    <div class="abs white" style="left:30px;top:154px;font-size:21px">Ingredientes</div>
    <div class="abs small" style="left:30px;top:183px">agua, malto de cervada, açucar de cana,<br>lupolo e leveduras.</div>
    <div class="divider" style="left:30px;top:249px;width:308px"></div>
    <div class="abs small" style="left:30px;top:275px">Fabricada e engarrafada for cervejaria<br>Velumar LTDA. Mão concelar.<br>Conservar em local frescos e arejado.<br>Aprecie com moderação.<br>Proibida venda para menores de 18 anos.<br>Indústria brasileira. Contem clútem.</div>
    <div class="sticker"></div>
  </div>

  <svg class="ribbon" style="left:0;top:0" width="1200" height="860" aria-hidden="true">
    <polygon points="596,770 700,770 700,837 596,837 632,803" fill="var(--ribbon-dark)"/>
    <polygon points="1125,770 1020,770 1020,837 1125,837 1089,803" fill="var(--ribbon-dark)"/>
    <rect x="652" y="757" width="415" height="62" fill="var(--ribbon)"/>
  </svg>
  <div class="ribbon-text quote-text">“NA VIDA, EXISTEM OUTRAS COISAS PARA ALÉM DE CERVEJA, MAS A CERVEJA FAZ ESSAS OUTRAS COISAS PARECEREM AINDA MELHORES.”</div>
</div>
</body>
</html>
```